Business Identity Stationary

Already have the logo which is in the attached files so only need the Business STationary
1) Double Sided Business Card
2) Letterhead
3) Presentation folder with business card holder on inside cover
4) WIth compliments slip
See information for business cards, letterhead and presentation folder below.
http://files.pixelbazaar-example.com/img/771204/40612/40612_3918825_771204_thumb.jpg
Updates

This should be a simply job using a logo we already had designed along with a little device. I suggest using the device off center and perhaps lower in the corner in an abstract way. Also the logo device could be used as a watermark for the letterhead. The designer who created the logo presented something that I think works well for a business card. The front of the double sided business card could have the name logo small for the website address and only use the Lime device on the front. Then on the back could be the name Brevar Consulting logo.

Please note that for the business card the black and lime green background do look good. Also please think of using the lime device separately in an unusual way.

It has been brought to my attention that.my budget was far to low. Hopefully this.will attract you to the project. 

The parent company of Brevar Consulting is TallHeron investments. I have uploaded a file of the Tall Heron business card I really like. Perhaps use this business card as a guide to the type of modern and clean style I am looking for. It also works to have the Brevar Consultign and Tall Heron similar.

Reason: Still haven't received anything exactly right.

Industry/Entity Type

Business

Font styles to use
Sans Serif

Colors
9bcb3c
000000
5c5c5c
add136
cadf82
eaf2cf
f9fbf2
1b1b1b
757575

Requirements
Must have
• 1) Double Sided Business Card
Marta Delvorin
Director
Tel: +505 8290 3357
Email: mkd@brevarconsulting-example.com
Website: www.brevarconsulting-example.com

Everett Delvorin
Director
Tel: +505 8290 3362
Email: ekd@brevarconsulting-example.com

Lucia Pardo Ventrosa
Director
Tel: 8442 6183
Email: lpv@brevarconsulting-example.com

2) Letterhead
Logo
Lime Logo Device
Website Address: www.brevarconsulting-example.com
Small print on bottom: Brevar Consulting a Tall Heron Investment Company SA. RUC K0720000483915

3) Presentation Folder
Traditional Presentation folder with inside front cover spot for the insertion of business card.

4) With Compliments slip

```html
<!DOCTYPE html>
<html lang="en">
<head>
<meta charset="utf-8">
<title>Brevar Consulting — Business Stationery</title>
<link href="https://fonts.googleapis.com/css2?family=Open+Sans:wght@400;600;700&display=swap" rel="stylesheet">
<style>
:root{
  --backdrop:#f5f9f0;
  --paper:#ffffff;
  --lime:#7ff226;
  --ink:#1b1b1b;
  --grey:#5c5c5c;
  --rule:#8a8a8a;
  --shadow:rgba(0,0,0,.35);
}
*{margin:0;padding:0;box-sizing:border-box}
html,body{width:1200px;height:1000px;overflow:hidden;background:var(--backdrop);font-family:"Open Sans",Arial,sans-serif;color:var(--ink)}
.canvas{position:relative;width:1200px;height:1000px}
.sheet{position:absolute;background:var(--paper);box-shadow:3px 4px 8px var(--shadow);overflow:hidden}
.sheet::after{content:"";position:absolute;left:0;right:0;bottom:0;height:6px;background:var(--lime)}
.wordmark{position:absolute;font-weight:700;color:var(--ink);line-height:1;letter-spacing:.5px}
.wordmark .line{display:block}
.wordmark--sm{font-size:15px}
.wordmark--sm .line+.line{font-size:10px;letter-spacing:2px;margin-top:1px}
.wordmark--md{font-size:22px}
.wordmark--md .line+.line{font-size:12px;letter-spacing:3px;margin-top:2px}
.wordmark--lg{font-size:46px;left:0;right:0;text-align:center;top:62px}
.wordmark--lg .line+.line{font-size:20px;letter-spacing:7px;margin-top:4px}
.footer-note{position:absolute;left:0;right:0;text-align:center;font-size:5.5px;font-weight:600;line-height:9px}
.folder-divider{position:absolute;left:381px;top:0;bottom:0;width:2px;background:var(--rule)}
.card-slot{position:absolute;left:542px;top:315px;width:159px;height:103px;border:1px solid var(--grey);padding:3px}
.mini-card{position:relative;width:100%;height:100%;border:1px solid #bbb;background:var(--paper);overflow:hidden}
.mini-card::after{content:"";position:absolute;left:0;right:0;bottom:0;height:4px;background:var(--lime)}
.mini-card .wordmark{left:6px;top:8px;font-size:10px}
.mini-card .wordmark .line+.line{font-size:6px;letter-spacing:1px}
.mini-card .name{position:absolute;left:6px;top:46px;font-size:6px;font-weight:700;color:var(--lime)}
.mini-card .role{position:absolute;left:6px;top:54px;font-size:5px;color:var(--lime)}
.mini-card .details{position:absolute;left:6px;top:64px;font-size:5px;line-height:7.5px;font-weight:600}
.compliments{position:absolute;left:66px;top:66px;font-size:7px;font-weight:700}
.slip-url{position:absolute;left:10px;top:186px;font-size:7px;font-weight:700}
.card .wordmark{left:10px;top:12px}
.card .name{position:absolute;left:8px;top:80px;font-size:11px;font-weight:700;color:var(--lime)}
.card .role{position:absolute;left:8px;top:96px;font-size:10px;color:var(--lime)}
.contact{position:absolute;left:8px;top:115px;list-style:none;font-size:9.5px;line-height:14.5px}
.contact li{display:flex;align-items:center;gap:7px;white-space:nowrap}
.contact svg{width:12px;height:10px;flex:none}
.card-back .dot{position:absolute;left:10px;top:10px;width:22px;height:22px;border-radius:50%;background:var(--lime)}
</style>
</head>
<body>
<div class="canvas">

  <!-- Letterhead -->
  <section class="sheet letterhead" style="left:24px;top:40px;width:372px;height:482px">
    <div class="wordmark wordmark--sm" style="left:16px;top:14px"><span class="line">BREVAR</span><span class="line">consulting</span></div>
    <p class="footer-note" style="top:457px">www.brevarconsulting-example.com<br>Brevar Consulting a Tall Heron Investment Company SA. RUC K0720000483915</p>
  </section>

  <!-- Presentation folder -->
  <section class="sheet folder" style="left:419px;top:40px;width:779px;height:482px">
    <div class="wordmark wordmark--sm" style="left:14px;top:14px"><span class="line">BREVAR</span><span class="line">consulting</span></div>
    <p class="footer-note" style="right:auto;width:381px;top:457px">www.brevarconsulting-example.com<br>Brevar Consulting a Tall Heron Investment Company SA. RUC K0720000483915</p>
    <div class="folder-divider"></div>
    <div class="wordmark wordmark--sm" style="left:395px;top:14px"><span class="line">BREVAR</span><span class="line">consulting</span></div>
    <div class="card-slot">
      <div class="mini-card">
        <div class="wordmark"><span class="line">BREVAR</span><span class="line">consulting</span></div>
        <p class="name">Marta Delvorin</p>
        <p class="role">Director</p>
        <p class="details">mkd@brevarconsulting-example.com<br>+505 8290 3357<br>www.brevarconsulting-example.com</p>
      </div>
    </div>
  </section>

  <!-- With compliments slip -->
  <section class="sheet slip" style="left:387px;top:555px;width:450px;height:205px">
    <div class="wordmark wordmark--md" style="left:10px;top:12px"><span class="line">BREVAR</span><span class="line">consulting</span></div>
    <p class="compliments">With Compliments,</p>
    <p class="slip-url">www.brevarconsulting-example.com</p>
  </section>

  <!-- Business cards -->
  <section class="sheet card" style="left:24px;top:792px;width:276px;height:172px">
    <div class="wordmark wordmark--md"><span class="line">BREVAR</span><span class="line">consulting</span></div>
    <p class="name">Marta Delvorin</p>
    <p class="role">Director</p>
    <ul class="contact">
      <li><svg viewBox="0 0 12 10"><rect x="0" y="1" width="12" height="8" fill="#7ff226"/><path d="M0 1l6 5 6-5" stroke="#fff" fill="none"/></svg>mkd@brevarconsulting-example.com</li>
      <li><svg viewBox="0 0 12 10"><rect x="3" y="0" width="6" height="10" rx="1" fill="#7ff226"/><rect x="4" y="1.5" width="4" height="5" fill="#fff"/></svg>+505 8290 3357</li>
      <li><svg viewBox="0 0 12 10"><circle cx="6" cy="5" r="4.5" fill="#7ff226"/><path d="M1.5 5h9M6 .5v9" stroke="#fff"/></svg>www.brevarconsulting-example.com</li>
    </ul>
  </section>

  <section class="sheet card" style="left:317px;top:792px;width:276px;height:172px">
    <div class="wordmark wordmark--md"><span class="line">BREVAR</span><span class="line">consulting</span></div>
    <p class="name">Everett Delvorin</p>
    <p class="role">Director</p>
    <ul class="contact">
      <li><svg viewBox="0 0 12 10"><rect x="0" y="1" width="12" height="8" fill="#7ff226"/><path d="M0 1l6 5 6-5" stroke="#fff" fill="none"/></svg>ekd@brevarconsulting-example.com</li>
      <li><svg viewBox="0 0 12 10"><rect x="3" y="0" width="6" height="10" rx="1" fill="#7ff226"/><rect x="4" y="1.5" width="4" height="5" fill="#fff"/></svg>+505 8290 3362</li>
      <li><svg viewBox="0 0 12 10"><circle cx="6" cy="5" r="4.5" fill="#7ff226"/><path d="M1.5 5h9M6 .5v9" stroke="#fff"/></svg>www.brevarconsulting-example.com</li>
    </ul>
  </section>

  <section class="sheet card" style="left:612px;top:792px;width:280px;height:172px">
    <div class="wordmark wordmark--md"><span class="line">BREVAR</span><span class="line">consulting</span></div>
    <p class="name">Lucia Pardo Ventrosa</p>
    <p class="role">Director</p>
    <ul class="contact">
      <li><svg viewBox="0 0 12 10"><rect x="0" y="1" width="12" height="8" fill="#7ff226"/><path d="M0 1l6 5 6-5" stroke="#fff" fill="none"/></svg>lpv@brevarconsulting-example.com</li>
      <li><svg viewBox="0 0 12 10"><rect x="3" y="0" width="6" height="10" rx="1" fill="#7ff226"/><rect x="4" y="1.5" width="4" height="5" fill="#fff"/></svg>+505 8442 6183</li>
      <li><svg viewBox="0 0 12 10"><circle cx="6" cy="5" r="4.5" fill="#7ff226"/><path d="M1.5 5h9M6 .5v9" stroke="#fff"/></svg>www.brevarconsulting-example.com</li>
    </ul>
  </section>

  <section class="sheet card-back" style="left:904px;top:792px;width:278px;height:172px">
    <span class="dot"></span>
    <div class="wordmark wordmark--lg"><span class="line">BREVAR</span><span class="line">consulting</span></div>
  </section>

</div>
</body>
</html>
```